Grand Chart of Bold Reformers

Hi - I would like your help transforming my (terrible) drawing into a graphic that pops -using hex colors I'll give you - so that I can put it into stationary and on t-shirts or tote bags. My company, the Marrowgate Institute, trains social change leaders (from the sectors in the periodic table) on how to lead large-scale change. I have this vision - the "periodic table" but these are the sectors that my clients work in. If you are having trouble reading my writing, I apologize. Our hex colors are: #114769, #76984C, #80B5CF (Seagull), #8F2C63 and Rangoon Black #191919. You don't need to use all of them, but it'd be good to be consistent with our overall branding. If you can't read my writing, I will send correct spelling. The "Marrowgate" with the flowers on the bottom is for a separate design bid.

Target Market(s)

nonprofit, social entrepreneurs, philanthropy, leaders

Requirements
Must have
• clean, readable font. alignment to look like periodic table of elements. heart icon for love, cat face for cats.

```html
<!DOCTYPE html>
<html lang="en">
<head>
<meta charset="utf-8">
<title>Grand Chart of Bold Reformers</title>
<link rel="stylesheet" href="https://fonts.googleapis.com/css2?family=Oranienbaum&display=swap">
<style>
  :root {
    --seagull: #80B5CF;
    --rangoon: #1B1B1B;
    --navy: #114769;
    --plum: #8F2C63;
    --paper: #FFFFFF;
    --ink-light: #FFFFFF;
  }
  html, body {
    margin: 0;
    padding: 0;
    width: 1200px;
    height: 1200px;
    overflow: hidden;
    background: var(--paper);
  }
  .chart {
    position: relative;
    width: 1200px;
    height: 1200px;
    font-family: "Oranienbaum", serif;
    color: var(--ink-light);
  }
  .tile {
    position: absolute;
    width: 136px;
    height: 136px;
    border-radius: 9px;
    background: var(--seagull);
    box-sizing: border-box;
  }
  .tile--dark { background: var(--rangoon); }
  .tile--navy { background: var(--navy); }
  .tile--plum { background: var(--plum); }
  .tile__label {
    position: absolute;
    top: 16px;
    left: 0;
    right: 0;
    height: 56px;
    display: flex;
    align-items: center;
    justify-content: center;
  }
  .tile__label span {
    display: block;
    font-size: 22px;
    line-height: 27px;
    text-align: left;
    white-space: nowrap;
    letter-spacing: 0.2px;
  }
  .tile__symbol {
    position: absolute;
    left: 17px;
    top: 84px;
    font-size: 31px;
    line-height: 1;
  }
  .tile__icon {
    position: absolute;
  }
  .icon-heart { left: 13px; top: 89px; width: 35px; height: 31px; }
  .icon-cat { left: 17px; top: 87px; width: 43px; height: 33px; border-radius: 40% 40% 48% 48%; background: var(--seagull); }

  .c1 { left: 155.6px; } .c2 { left: 307.5px; } .c3 { left: 459.4px; }
  .c4 { left: 611.3px; } .c5 { left: 763.1px; } .c6 { left: 915px; }
  .r1 { top: 191px; } .r2 { top: 343px; } .r3 { top: 495px; }
  .r4 { top: 647px; } .r5 { top: 880px; }
</style>
</head>
<body>
<main class="chart">
  <!-- Row 1 -->
  <div class="tile c1 r1"><div class="tile__label"><span>Anti-<br>violence</span></div><div class="tile__symbol">Av</div></div>
  <div class="tile c6 r1"><div class="tile__label"><span>Belonging</span></div><div class="tile__symbol">B</div></div>

  <!-- Row 2 -->
  <div class="tile c1 r2"><div class="tile__label"><span>Early<br>childho</span></div><div class="tile__symbol">Ec</div></div>
  <div class="tile c2 r2"><div class="tile__label"><span>Climate<br>change</span></div><div class="tile__symbol">Cc</div></div>
  <div class="tile c3 r2"><div class="tile__label"><span>Environment<br>justice</span></div><div class="tile__symbol">Ej</div></div>
  <div class="tile tile--dark c4 r2"><div class="tile__label"><span>Human<br>-----</span></div><div class="tile__symbol">Hs</div></div>
  <div class="tile c5 r2"><div class="tile__label"><span>Health<br>care</span></div><div class="tile__symbol">Hc</div></div>
  <div class="tile c6 r2"><div class="tile__label"><span>Housing</span></div><div class="tile__symbol">Ec</div></div>

  <!-- Row 3 -->
  <div class="tile tile--dark c1 r3"><div class="tile__label"><span>Education</span></div><div class="tile__symbol">Ed</div></div>
  <div class="tile c2 r3"><div class="tile__label"><span>Attend<br>school</span></div><div class="tile__symbol">As</div></div>
  <div class="tile c3 r3"><div class="tile__label"><span>Social<br>justice</span></div><div class="tile__symbol">Sj</div></div>
  <div class="tile tile--dark c4 r3"><div class="tile__label"><span>Civil<br>rishd</span></div><div class="tile__symbol">Cr</div></div>
  <div class="tile c5 r3"><div class="tile__label"><span>Health<br>equity</span></div><div class="tile__symbol">He</div></div>
  <div class="tile tile--dark c6 r3"><div class="tile__label"><span>Jobs</span></div><div class="tile__symbol">J</div></div>

  <!-- Row 4 -->
  <div class="tile c1 r4"><div class="tile__label"><span>Animal<br>welfare</span></div><div class="tile__symbol">Aw</div></div>
  <div class="tile tile--navy c2 r4"><div class="tile__label"><span>Cats</span></div><div class="tile__icon icon-cat" role="img" aria-label="Cat face icon"></div></div>
  <div class="tile c3 r4"><div class="tile__label"><span>Racial<br>justice</span></div><div class="tile__symbol">Rj</div></div>
  <div class="tile tile--dark c4 r4"><div class="tile__label"><span>-----<br>rishd</span></div><div class="tile__symbol">Jr</div></div>
  <div class="tile c5 r4"><div class="tile__label"><span>Behavioral<br>health</span></div><div class="tile__symbol">Bh</div></div>
  <div class="tile tile--dark c6 r4"><div class="tile__label"><span>Inter-<br>generational</span></div><div class="tile__symbol">Ig</div></div>

  <!-- Values row -->
  <div class="tile tile--plum c1 r5"><div class="tile__label"><span>Love</span></div>
    <svg class="tile__icon icon-heart" viewBox="0 0 36 32" role="img" aria-label="Heart">
      <path d="M18 31 C 7 23 0 17 0 9.5 C 0 4 4 0 9 0 C 13 0 16 2.5 18 5.5 C 20 2.5 23 0 27 0 C 32 0 36 4 36 9.5 C 36 17 29 23 18 31 Z" fill="#FFFFFF"/>
    </svg>
  </div>
  <div class="tile c2 r5"><div class="tile__label"><span>Authenticity</span></div><div class="tile__symbol">A</div></div>
  <div class="tile c3 r5"><div class="tile__label"><span>Humility</span></div><div class="tile__symbol">H</div></div>
  <div class="tile tile--dark c4 r5"><div class="tile__label"><span>Audacity</span></div><div class="tile__symbol">Au</div></div>
  <div class="tile c5 r5"><div class="tile__label"><span>Justice</span></div><div class="tile__symbol">J</div></div>
</main>
</body>
</html>
```